Harrow Glen Whiskey Label

We are looking for a label to be made for our single batch whiskey. in the attached pdf you will see the lay out of the design. We are going to use a whiskey bottle with a cork. Some of the label you will need to leave some space for hand writing.

Target Market(s)

people who like craft beer and whiskey

Industry/Entity Type

Craft Distillery

Font styles to use
Decorative

Colors

Designer to choose colors to be used in the design.

Requirements
Must have
• room for hand writing informatiom

```html
<!DOCTYPE html>
<html lang="en">
<head>
<meta charset="utf-8">
<title>Harrow Glen Whisky Label</title>
<link rel="stylesheet" href="https://fonts.googleapis.com/css2?family=Oranienbaum&family=Rye&family=Dancing+Script:wght@700&family=Zilla+Slab:wght@700&display=swap">
<style>
  :root {
    --cream: #fff6cf;
    --ink: #2e2e2e;
    --frame-top: #fdae3f;
    --frame-bottom: #ffff00;
    --footer-band: #706e60;
    --footer-text: #fff6cf;
    --banner-tone: #efe3b8;
  }
  * { margin: 0; padding: 0; box-sizing: border-box; }
  html, body { width: 800px; height: 1200px; overflow: hidden; background: var(--cream); }
  .label {
    position: relative;
    width: 800px;
    height: 1200px;
    background: var(--cream);
    color: var(--ink);
  }
  .label-frame {
    position: absolute;
    left: 13px; top: 13px; width: 774px; height: 1172px;
    border: 10px solid transparent;
    border-image: linear-gradient(to bottom, var(--frame-top), var(--frame-bottom)) 1;
  }
  .distillery-name {
    position: absolute;
    top: 120px; left: 0; width: 800px;
    text-align: center;
    font-family: "Oranienbaum", serif;
    font-size: 64px;
    line-height: 1;
    font-weight: 400;
    -webkit-text-stroke: 1.2px var(--ink);
  }
  .ribbon-banner {
    position: absolute;
    left: 53px; top: 212px; width: 697px; height: 125px;
  }
  .ribbon-art {
    position: absolute; inset: 0;
    background: var(--banner-tone);
    border-radius: 14px;
  }
  .product-name {
    position: absolute;
    top: 16px; left: 0; width: 100%;
    text-align: center;
    font-family: "Dancing Script", cursive;
    font-size: 62px;
    line-height: 1.3;
    color: var(--ink);
  }
  .spirit-type {
    position: absolute;
    left: 160px; top: 340px; width: 484px; height: 140px;
  }
  .spirit-type text {
    font-family: "Rye", serif;
    font-size: 170px;
    fill: var(--ink);
  }
  .title-rule {
    position: absolute;
    left: 168px; top: 492px; width: 468px; height: 3px;
    background: var(--ink);
  }
  .mash-note {
    position: absolute;
    top: 508px; left: 0; width: 800px;
    text-align: center;
    font-family: "Zilla Slab", serif;
    font-weight: 700;
    font-size: 34px;
    letter-spacing: 1px;
  }
  .batch-table {
    position: absolute;
    left: 46px; top: 607px; width: 708px; height: 226px;
    border-collapse: collapse;
    font-family: "Zilla Slab", serif;
    font-weight: 700;
    font-size: 22px;
  }
  .batch-table td {
    border: 2px solid var(--ink);
    padding: 0 18px;
    vertical-align: middle;
    width: 50%;
  }
  .batch-table .row-wide td { height: 79px; }
  .batch-table .row-fields td { height: 73px; }
  .batch-table .col-right { padding-left: 26px; }
  .volume {
    position: absolute;
    right: 50px; top: 866px;
    font-family: "Zilla Slab", serif;
    font-weight: 700;
    font-size: 62px;
    line-height: 1;
  }
  .producer-band {
    position: absolute;
    left: 46px; top: 957px; width: 708px; height: 161px;
    background: var(--footer-band);
    color: var(--footer-text);
    font-family: "Oranienbaum", serif;
    font-size: 36px;
    line-height: 37px;
    text-align: center;
    padding-top: 17px;
    text-transform: uppercase;
    -webkit-text-stroke: 0.6px var(--footer-text);
  }
</style>
</head>
<body>
<main class="label">
  <div class="label-frame"></div>

  <h1 class="distillery-name">Iron Spur Distillery</h1>

  <div class="ribbon-banner">
    <div class="ribbon-art" role="img" aria-label="Engraved scroll ribbon banner carrying the product name"></div>
    <p class="product-name">Harrow Glen</p>
  </div>

  <svg class="spirit-type" viewBox="0 0 484 140" aria-label="Whisky">
    <text x="8" y="134" textLength="468" lengthAdjust="spacingAndGlyphs">WHISKY</text>
  </svg>

  <div class="title-rule"></div>

  <p class="mash-note">Malt Mash And Hops</p>

  <table class="batch-table">
    <tr class="row-wide"><td colspan="2">Harrow Glen Whisky Made</td></tr>
    <tr class="row-fields"><td>Aged:</td><td class="col-right">% ALC. BY VOL.</td></tr>
    <tr class="row-fields"><td>BOTTLE:</td><td class="col-right">OF:</td></tr>
  </table>

  <p class="volume">750ml</p>

  <footer class="producer-band">
    Distilled and bottle by<br>
    Iron Spur Distillery LLC<br>
    48 Larkin St.&nbsp; Alder Falls NJ 08112
  </footer>
</main>
</body>
</html>
```